RVT 2023 Postcard

We need a postcard created for an upcoming trade show. We had something made for our sister company a while back and are interested in a similar look. We have included images and some layouts that can be used along with our logo. We like earthy colors, gray and black are okay too. We would like it to be 5x7 and landscape orientation. We have attached the wording we would like to see on the back of the card with changes made in red.
Target Market(s)
retailers
Industry/Entity Type
wedding ring
Colors
Designer to choose only greyscale colors for use in the design.
Look and feel

```html
<!DOCTYPE html>
<html lang="en">
<head>
<meta charset="utf-8">
<title>Orrin Bands – Trade Show Postcard</title>
<link rel="stylesheet" href="https://fonts.googleapis.com/css2?family=Cinzel:wght@400;600&family=Cabin:wght@400;500&family=Montserrat:wght@400&display=swap">
<style>
  :root {
    --backdrop: #575555;
    --card-dark: #0b0b0c;
    --card-mid: #2a2a2c;
    --card-light: #5b5b5e;
    --ink: #ffffff;
    --ink-soft: #e6e6e6;
    --rule: #cfcfcf;
  }
  * { margin: 0; padding: 0; box-sizing: border-box; }
  html, body { width: 1200px; height: 1200px; overflow: hidden; }
  body { background: var(--backdrop); position: relative; font-family: "Cabin", sans-serif; color: var(--ink); }

  .card { position: absolute; left: 246px; width: 708px; height: 506px; overflow: hidden; }
  .card-front { top: 52px;
    background: radial-gradient(ellipse at 95% 75%, var(--card-light) 0%, var(--card-mid) 30%, var(--card-dark) 70%); }
  .card-back { top: 631px;
    background: radial-gradient(ellipse at 0% 40%, var(--card-light) 0%, var(--card-mid) 30%, var(--card-dark) 75%); }

  .front-photo { position: absolute; inset: 0;
    background:
      radial-gradient(ellipse 90px 130px at 36% 50%, #d8d8d8 0%, #9a9a9a 55%, transparent 75%),
      radial-gradient(ellipse 90px 130px at 64% 50%, #e6c76c 0%, #b08f33 55%, transparent 75%); }

  .brand { position: absolute; left: 45px; top: 32px; width: 96px; text-align: center; }
  .brand-square { width: 58px; height: 58px; border: 3px solid var(--ink); margin: 0 auto 10px; }
  .brand-name { font-family: "Cabin", sans-serif; font-weight: 400; font-size: 15px; letter-spacing: 1px; color: var(--ink); }

  .ring-stack { position: absolute; left: 19px; top: 164px; width: 165px; height: 307px;
    background: linear-gradient(170deg, #cfcfcf 0%, #9d9d9d 50%, #c79a86 75%, #bdbdbd 100%);
    border-radius: 40px; opacity: .85; }

  .headline { position: absolute; left: 198px; top: 30px; font-family: "Cinzel", serif; font-weight: 600;
    font-size: 26px; letter-spacing: .5px; white-space: nowrap; }

  .benefits { position: absolute; left: 197px; top: 78px; list-style: none; }
  .benefits li { font-size: 15.5px; line-height: 24.4px; white-space: nowrap; display: flex; align-items: center; }
  .benefits li::before { content: ""; width: 9px; height: 9px; border: 1.3px solid var(--ink); border-radius: 50%; margin-right: 8px; }

  .tagline-box { position: absolute; left: 197px; top: 245px; width: 476px; height: 32px; border: 1px solid var(--ink);
    font-family: "Cinzel", serif; font-size: 19px; text-align: center; line-height: 30px; letter-spacing: .5px; }
  .call { position: absolute; left: 197px; top: 284px; width: 476px; text-align: center; font-size: 16px; }
  .call strong { font-weight: 500; }

  .features { position: absolute; left: 199px; top: 333px; display: grid; grid-template-columns: 281px 200px;
    row-gap: 6px; list-style: none; }
  .features li { font-family: "Cinzel", serif; font-size: 14.5px; height: 19.5px; white-space: nowrap;
    display: flex; align-items: center; gap: 6px; }
  .features svg { width: 11px; height: 11px; flex: none; }

  .footer-rule { position: absolute; left: 197px; top: 447px; width: 477px; border-top: 1px solid var(--rule); }
  .contact { position: absolute; left: 197px; width: 477px; text-align: center; font-family: "Montserrat", sans-serif;
    font-size: 11.3px; color: var(--ink-soft); white-space: nowrap; }
  .contact-address { top: 458px; }
  .contact-web { top: 476px; }
  .contact svg { width: 10px; height: 10px; vertical-align: -1px; margin-right: 2px; }
</style>
</head>
<body>
  <section class="card card-front">
    <div class="front-photo" role="img" aria-label="Product photo: an engraved leaf-pattern white gold band beside a polished yellow gold band on a dark background"></div>
  </section>

  <section class="card card-back">
    <div class="brand">
      <div class="brand-square"></div>
      <div class="brand-name">ORRIN BANDS</div>
    </div>
    <div class="ring-stack" role="img" aria-label="Product photo: a stack of wedding bands in white, rose and yellow gold, some set with diamonds"></div>

    <h1 class="headline">PREMIUM CUSTOMIZED PROGRAMS</h1>
    <ul class="benefits">
      <li>Promote your own brand, rings stamped with your specified logo</li>
      <li>Offer rings in any width, 3 thicknesses and all precious metals</li>
      <li>Combine &amp; customize 5500 ring designs</li>
      <li>Sell in Platinum, 18kt, 14kt &amp; 10kt</li>
      <li>Samples kits starting as low as $900</li>
      <li>Program Performance Money Back Guarantee</li>
    </ul>

    <div class="tagline-box">YOUR TRUSTED SOURCE FOR RINGS</div>
    <p class="call">Call <strong>800.555.0199</strong> for more information</p>

    <ul class="features">
      <li><svg viewBox="0 0 12 12"><circle cx="6" cy="6" r="5.2" fill="none" stroke="#fff" stroke-width="1"/><path d="M3.5 6.2l1.7 1.7 3.3-3.6" fill="none" stroke="#fff" stroke-width="1"/></svg>EASY PRICING SYSTEM</li>
      <li><svg viewBox="0 0 12 12"><circle cx="6" cy="6" r="5.2" fill="none" stroke="#fff" stroke-width="1"/><path d="M3.5 6.2l1.7 1.7 3.3-3.6" fill="none" stroke="#fff" stroke-width="1"/></svg>FREE SHIPPING</li>
      <li><svg viewBox="0 0 12 12"><circle cx="6" cy="6" r="5.2" fill="none" stroke="#fff" stroke-width="1"/><path d="M3.5 6.2l1.7 1.7 3.3-3.6" fill="none" stroke="#fff" stroke-width="1"/></svg>SCRAP BUYOUT OPTIONS</li>
      <li><svg viewBox="0 0 12 12"><circle cx="6" cy="6" r="5.2" fill="none" stroke="#fff" stroke-width="1"/><path d="M3.5 6.2l1.7 1.7 3.3-3.6" fill="none" stroke="#fff" stroke-width="1"/></svg>PRE-TAGGED SAMPLES</li>
      <li><svg viewBox="0 0 12 12"><circle cx="6" cy="6" r="5.2" fill="none" stroke="#fff" stroke-width="1"/><path d="M3.5 6.2l1.7 1.7 3.3-3.6" fill="none" stroke="#fff" stroke-width="1"/></svg>1 WEEK TURNAROUND</li>
      <li><svg viewBox="0 0 12 12"><circle cx="6" cy="6" r="5.2" fill="none" stroke="#fff" stroke-width="1"/><path d="M3.5 6.2l1.7 1.7 3.3-3.6" fill="none" stroke="#fff" stroke-width="1"/></svg>COMPETITIVE PRICING</li>
      <li><svg viewBox="0 0 12 12"><circle cx="6" cy="6" r="5.2" fill="none" stroke="#fff" stroke-width="1"/><path d="M3.5 6.2l1.7 1.7 3.3-3.6" fill="none" stroke="#fff" stroke-width="1"/></svg>FAMILY OWNED AND OPERATED</li>
      <li><svg viewBox="0 0 12 12"><circle cx="6" cy="6" r="5.2" fill="none" stroke="#fff" stroke-width="1"/><path d="M3.5 6.2l1.7 1.7 3.3-3.6" fill="none" stroke="#fff" stroke-width="1"/></svg>MADE PROUDLY IN USA</li>
    </ul>

    <div class="footer-rule"></div>
    <p class="contact contact-address">140 Larkfield Road, Elm Hollow NY 11020 &nbsp;
      <svg viewBox="0 0 12 12"><path d="M2.5 1.5l2 0 1 2.5-1.3 1a6 6 0 0 0 2.8 2.8l1-1.3 2.5 1v2a1 1 0 0 1-1 1A9 9 0 0 1 1.5 2.5a1 1 0 0 1 1-1z" fill="none" stroke="#e6e6e6" stroke-width="1"/></svg>718.555.0142 | &nbsp;800.555.0199</p>
    <p class="contact contact-web">
      <svg viewBox="0 0 12 12"><rect x="1" y="2.5" width="10" height="7" fill="none" stroke="#e6e6e6" stroke-width="1"/><path d="M1 2.5l5 4 5-4" fill="none" stroke="#e6e6e6" stroke-width="1"/></svg>sales@orrinbands.com &nbsp;| &nbsp;<svg viewBox="0 0 12 12"><circle cx="6" cy="6" r="5" fill="none" stroke="#e6e6e6" stroke-width="1"/><ellipse cx="6" cy="6" rx="2.2" ry="5" fill="none" stroke="#e6e6e6" stroke-width="1"/><path d="M1 6h10" stroke="#e6e6e6" stroke-width="1"/></svg>www.orrinbands.com &nbsp;&nbsp; OrrinBandsCo</p>
  </section>
</body>
</html>
```